Clean business card with logo provided

I want a card that will stand out among the masses. I need the color and image to show professionalism and yet have a family appeal showing that I only deal with win/win scenarios. The back of the card will be used to take notes about the individual so I can use that in my database entry. I like modern design but need professionalism in it also. It needs to fit my "clean, safe, and affordable housing" motto. I need to be able to write on the file and update the card details for my employees.

Target Market(s)

Investors looking to make investment income through real estate

Industry/Entity Type

Real Estate

Contact Information for Business Card

Troy Vandemark
blank address, city, st, zip code
480-555-0147
troyvandemark@quillrentals.example
www.quillrentals.example

Font styles to use
Sans Serif

Requirements
Must have
• I would like the back of the card to have lines for info. example
• Met/Visited: Date:
• Interets:
Nice to have
• I want the cards color to match the logo background color. Font with details to be san serif and black. I want the card rectangular with square corners. Standard business card size. I would like to see cards designed with both images to see which i prefer more.

```html
<!DOCTYPE html>
<html lang="en">
<head>
<meta charset="UTF-8">
<title>Quill Rentals LLC – Business Card</title>
<link rel="stylesheet" href="https://fonts.googleapis.com/css2?family=Open+Sans:wght@400;600;700&display=swap">
<style>
  :root {
    --backdrop: #3b3431;
    --card-black: #121212;
    --note-white: #ffffff;
    --accent-cyan: #2cb5d1;
    --text-light: #e6e6e6;
    --rule-grey: #5a5a5a;
    --line-dark: #444444;
  }
  * { box-sizing: border-box; margin: 0; padding: 0; }
  html, body { width: 1200px; height: 814px; overflow: hidden; }
  body {
    background: var(--backdrop);
    font-family: "Open Sans", sans-serif;
    position: relative;
  }
  .card {
    position: absolute;
    top: 252px;
    width: 540px;
    height: 309px;
    overflow: hidden;
  }
  .card--front { left: 40px; background: var(--card-black); }
  .card--back { left: 620px; background: var(--note-white); }

  .brand {
    position: absolute;
    color: var(--accent-cyan);
  }
  .brand__name {
    display: flex;
    align-items: center;
    gap: 7px;
    font-weight: 600;
    font-size: 17px;
    letter-spacing: 1px;
    white-space: nowrap;
  }
  .brand__dot {
    width: 9px; height: 9px; border-radius: 50%;
    background: var(--accent-cyan);
    flex: none;
  }
  .brand__motto {
    margin-top: 4px;
    font-size: 7.5px;
    color: var(--accent-cyan);
    letter-spacing: 0.3px;
    white-space: nowrap;
  }
  .card--front .brand { left: 28px; top: 138px; }

  .divider {
    position: absolute;
    left: 252px; top: 70px;
    width: 1px; height: 170px;
    background: var(--rule-grey);
  }
  .contact {
    position: absolute;
    left: 270px; top: 84px;
    color: var(--text-light);
    font-size: 12px;
    line-height: 21px;
  }
  .contact__name {
    color: var(--accent-cyan);
    font-weight: 700;
    font-size: 18px;
    line-height: 26px;
    margin-bottom: 2px;
  }
  .contact__row { display: flex; align-items: center; gap: 8px; white-space: nowrap; }
  .contact__row svg { width: 12px; height: 12px; flex: none; fill: var(--accent-cyan); }
  .contact__row .icon-mail { fill: none; stroke: var(--accent-cyan); stroke-width: 2; }

  .back__band {
    position: absolute; left: 0; top: 0;
    width: 100%; height: 86px;
    background: var(--card-black);
  }
  .card--back .brand { left: 170px; top: 24px; }
  .notes { position: absolute; left: 0; top: 86px; width: 100%; }
  .notes__row {
    position: absolute;
    left: 30px; right: 30px;
    display: flex; align-items: flex-end; gap: 6px;
    height: 24px;
  }
  .notes__label {
    color: var(--accent-cyan);
    font-size: 14px;
    font-weight: 600;
    white-space: nowrap;
    line-height: 18px;
  }
  .notes__line { flex: 1; border-bottom: 1px solid var(--line-dark); height: 1px; margin-bottom: 3px; }
  .notes__row--blank { left: 200px; }
</style>
</head>
<body>

<section class="card card--front" aria-label="Business card front">
  <div class="brand">
    <div class="brand__name"><span class="brand__dot"></span>QUILL RENTALS LLC</div>
    <div class="brand__motto">Providing clean, safe, and affordable housing</div>
  </div>
  <div class="divider"></div>
  <div class="contact">
    <div class="contact__name">Troy Vandemark</div>
    <div class="contact__row">1420 Alder Court</div>
    <div class="contact__row">Fairview, Alaska 34512</div>
    <div class="contact__row">
      <svg viewBox="0 0 24 24"><path d="M6.6 10.8a15.1 15.1 0 0 0 6.6 6.6l2.2-2.2a1 1 0 0 1 1-.25 11.4 11.4 0 0 0 3.6.57 1 1 0 0 1 1 1V20a1 1 0 0 1-1 1A17 17 0 0 1 3 4a1 1 0 0 1 1-1h3.5a1 1 0 0 1 1 1c0 1.25.2 2.45.57 3.57a1 1 0 0 1-.25 1z"/></svg>
      480-555-0147
    </div>
    <div class="contact__row">
      <svg viewBox="0 0 24 24" class="icon-mail"><path d="M2 5h20v14H2z M3 6l9 7 9-7"/></svg>
      troyvandemark@quillrentals.example
    </div>
    <div class="contact__row">
      <svg viewBox="0 0 24 24"><circle cx="12" cy="12" r="10"/></svg>
      www.quillrentals.example
    </div>
  </div>
</section>

<section class="card card--back" aria-label="Business card back, note lines">
  <div class="back__band"></div>
  <div class="brand">
    <div class="brand__name"><span class="brand__dot"></span>QUILL RENTALS LLC</div>
    <div class="brand__motto">Providing clean, safe, and affordable housing</div>
  </div>
  <div class="notes">
    <div class="notes__row notes__row--blank" style="top:6px"><span class="notes__line"></span></div>
    <div class="notes__row notes__row--blank" style="top:34px"><span class="notes__line"></span></div>
    <div class="notes__row notes__row--blank" style="top:62px"><span class="notes__line"></span></div>
    <div class="notes__row" style="top:96px"><span class="notes__label">MET/VISITED:</span><span class="notes__line"></span></div>
    <div class="notes__row" style="top:128px"><span class="notes__label">DATE:</span><span class="notes__line"></span></div>
    <div class="notes__row" style="top:160px"><span class="notes__label">INTERESTS:</span><span class="notes__line"></span></div>
    <div class="notes__row" style="top:192px;left:130px"><span class="notes__line"></span></div>
  </div>
</section>

</body>
</html>
```